" A Trilo Sistemas é uma empresa que desenvolve sistemas de monitoramento remoto, telemetria via satélite, telecontrole, automaçao, rastreamento de veículos e etc.. Trata-se de uma empresa moderna e jovem, com uma linguagem de comunicaçao moderna e descontraída, sem perder a seriedade. Temos dois segmentos: Corporativo e Varejo. No corporativo, prestamos serviço para grandes empresas como Pedra Alta Minérios por exemplo.Já no varejo atendemos pessoas fisicas ou pequenas empresas. "

```html
<!DOCTYPE html>
<html lang="pt-BR">
<head>
<meta charset="utf-8">
<title>Trilo Sistemas — Clientes, Portfólio e Contato</title>
<link href="https://fonts.googleapis.com/css2?family=Ubuntu:wght@300;400;500;700&display=swap" rel="stylesheet">
<style>
  :root {
    --navy: #1d4862;
    --navy-deep: #1a4a66;
    --orange: #e0773a;
    --orange-btn: #e0642a;
    --white: #ffffff;
    --card-bg: #f7f7f7;
    --line: #d9d9d9;
    --text: #555555;
    --muted: #9a9a9a;
    --green: #5cb85c;
    --red: #d9372b;
  }
  * { box-sizing: border-box; margin: 0; padding: 0; }
  html, body { width: 1200px; height: 1200px; overflow: hidden; background: var(--white); }
  body { position: relative; font-family: "Ubuntu", Arial, sans-serif; color: var(--text); }
  .abs { position: absolute; }

  .section-title {
    position: absolute; left: 0; width: 1200px; text-align: center;
    font-weight: 700; font-size: 46px; letter-spacing: 1px; color: var(--navy);
  }
  .clients-title { top: 16px; }
  .contact-title { top: 736px; }

  .arrow-btn {
    position: absolute; top: 102px; width: 42px; height: 42px;
    border: 3px solid var(--navy); border-radius: 50%;
  }
  .arrow-btn svg { display: block; }
  .client-logo {
    position: absolute; top: 89px; width: 120px; height: 72px;
    background: #ececec; display: flex; align-items: center; justify-content: center;
    font-weight: 500; font-size: 19px; color: var(--navy);
  }

  .portfolio {
    position: absolute; left: 223px; top: 204px; width: 756px; height: 511px;
    background: var(--orange);
  }
  .portfolio-title {
    position: absolute; left: 0; top: 22px; width: 100%; text-align: center;
    color: var(--white); font-weight: 500; font-size: 46px; letter-spacing: 1px;
  }
  .portfolio-lead {
    position: absolute; left: 40px; top: 80px; width: 680px; text-align: center;
    color: var(--white); font-weight: 300; font-size: 28px; line-height: 34px;
  }
  .project-tile { position: absolute; width: 211px; height: 156px; overflow: hidden; }
  .tile-label {
    position: absolute; left: 0; bottom: 0; width: 100%; height: 30px;
    background: rgba(22, 60, 84, 0.9); color: var(--white);
    font-size: 10px; font-weight: 500; line-height: 30px; text-align: center; letter-spacing: .3px;
  }
  .tile-plus { position: absolute; left: 93px; top: 50px; }

  .channel-card {
    position: absolute; top: 811px; width: 156px; height: 118px;
    background: var(--card-bg); box-shadow: 0 1px 3px rgba(0,0,0,.12);
    text-align: center;
  }
  .channel-card svg { position: absolute; left: 50%; top: 12px; transform: translateX(-50%); }
  .channel-text {
    position: absolute; left: 8px; right: 8px; top: 78px;
    font-size: 10px; line-height: 12px; color: var(--text);
  }
  .channel-phone { top: 88px; font-size: 14px; font-weight: 500; color: #333; }

  .form-lead { position: absolute; left: 259px; top: 938px; font-size: 17px; color: var(--text); }
  .field {
    position: absolute; left: 259px; width: 336px; height: 35px;
    border: 1px solid var(--line); background: var(--white);
    font-size: 13px; line-height: 33px; padding-left: 14px; color: var(--muted);
  }
  .field svg { position: absolute; right: 10px; top: 9px; }
  .field-error {
    position: absolute; right: 34px; top: 0; font-size: 9px; color: var(--red); font-weight: 500;
  }
  .message-box {
    position: absolute; left: 612px; top: 970px; width: 324px; height: 86px;
    border: 1px solid var(--line); font-size: 13px; color: var(--muted); padding: 10px 12px;
  }
  .submit-btn {
    position: absolute; left: 612px; top: 1066px; width: 161px; height: 38px;
    background: var(--orange-btn); color: var(--white); border-radius: 3px;
    font-weight: 700; font-size: 17px; line-height: 38px; text-align: center; letter-spacing: .5px;
  }

  .footer-bar {
    position: absolute; left: 257px; top: 1152px; width: 686px; height: 48px;
    background: var(--navy-deep); border-radius: 4px 4px 0 0;
    display: flex; align-items: center; justify-content: center; gap: 10px;
    color: var(--white); font-weight: 500; font-size: 26px;
  }
  .footer-mark { width: 24px; height: 24px; border-radius: 50%; background: var(--white); }
</style>
</head>
<body>

  <h2 class="section-title clients-title">CLIENTES</h2>

  <div class="arrow-btn" style="left:280px;">
    <svg width="36" height="36" viewBox="0 0 36 36"><path d="M21 10 L13 18 L21 26" fill="none" stroke="#1d4862" stroke-width="3.5" stroke-linecap="round" stroke-linejoin="round"/></svg>
  </div>
  <div class="client-logo" style="left:336px;">Lumen</div>
  <div class="client-logo" style="left:468px;">Kaito</div>
  <div class="client-logo" style="left:600px;">Mercalto</div>
  <div class="client-logo" style="left:732px;">Petrolux</div>
  <div class="arrow-btn" style="left:862px;">
    <svg width="36" height="36" viewBox="0 0 36 36"><path d="M15 10 L23 18 L15 26" fill="none" stroke="#1d4862" stroke-width="3.5" stroke-linecap="round" stroke-linejoin="round"/></svg>
  </div>

  <section class="portfolio">
    <h2 class="portfolio-title">PORTFÓLIO</h2>
    <p class="portfolio-lead">Conheça um pouco mais sobre o que fazemos e o que já fizemos.</p>

    <div class="project-tile" style="left:48px; top:151px; background:linear-gradient(180deg,#8aa6c2 0%,#7b7f78 55%,#6a5d48 100%);" role="img" aria-label="Foto de obra com máquina escavadeira">
      <svg class="tile-plus" width="24" height="24" viewBox="0 0 24 24"><path d="M12 3v18M3 12h18" stroke="#fff" stroke-width="4"/></svg>
      <div class="tile-label">NOME DA EMPRESA/ DO PROJETO</div>
    </div>
    <div class="project-tile" style="left:276px; top:151px; background:linear-gradient(180deg,#c9a875 0%,#8f7a4e 40%,#4e6a2c 70%,#6a4a2c 100%);" role="img" aria-label="Foto de trator em plantação ao entardecer"></div>
    <div class="project-tile" style="left:502px; top:151px; background:linear-gradient(180deg,#e8e6e2 0%,#9a9da3 50%,#2f3440 100%);" role="img" aria-label="Foto de equipe de executivos sorrindo"></div>

    <div class="project-tile" style="left:48px; top:319px; background:linear-gradient(180deg,#f1f0ee 0%,#a3a6ab 50%,#2c313b 100%);" role="img" aria-label="Foto de equipe de executivos de braços cruzados"></div>
    <div class="project-tile" style="left:276px; top:319px; background:linear-gradient(180deg,#3c5b82 0%,#d79b3f 45%,#a1612a 70%,#3d3a22 100%);" role="img" aria-label="Foto de colheitadeira no campo ao pôr do sol"></div>
    <div class="project-tile" style="left:502px; top:319px; background:linear-gradient(180deg,#a84a14 0%,#e08a2a 45%,#5a2a0c 80%,#1c0e06 100%);" role="img" aria-label="Foto de torres de transmissão de energia ao pôr do sol"></div>
  </section>

  <h2 class="section-title contact-title">CONTATO</h2>

  <div class="channel-card" style="left:259px;">
    <svg width="50" height="58" viewBox="0 0 50 58">
      <rect x="6" y="8" width="32" height="42" rx="3" fill="none" stroke="#e0642a" stroke-width="3.5"/>
      <rect x="15" y="3" width="14" height="9" rx="2" fill="#e0642a"/>
      <path d="M13 22h18M13 30h18M13 38h12" stroke="#e0642a" stroke-width="3"/>
      <circle cx="38" cy="46" r="10" fill="#e0642a"/>
      <path d="M33 46l4 4 6-7" fill="none" stroke="#fff" stroke-width="2.5"/>
    </svg>
    <p class="channel-text">Complete o formulário abaixo, é super rápido :)</p>
  </div>

  <div class="channel-card" style="left:437px;">
    <svg width="56" height="56" viewBox="0 0 56 56">
      <path d="M28 8c-12 0-22 8-22 18 0 6 3 11 8 14l-3 9 10-6c2 .5 4 1 7 1 12 0 22-8 22-18S40 8 28 8z" fill="none" stroke="#e0642a" stroke-width="4" stroke-linejoin="round"/>
    </svg>
    <p class="channel-text">Mande um email para nós iremos te responder.</p>
  </div>

  <div class="channel-card" style="left:612px;">
    <svg width="56" height="58" viewBox="0 0 56 58">
      <circle cx="28" cy="24" r="13" fill="#e0642a"/>
      <path d="M12 26v-4a16 16 0 0 1 32 0v4" fill="none" stroke="#e0642a" stroke-width="4"/>
      <rect x="8" y="22" width="7" height="12" rx="3" fill="#e0642a"/>
      <rect x="41" y="22" width="7" height="12" rx="3" fill="#e0642a"/>
      <path d="M10 56c2-10 9-15 18-15s16 5 18 15z" fill="#e0642a"/>
    </svg>
    <p class="channel-text">Bate papo online fale conosco agora mesmo.</p>
  </div>

  <div class="channel-card" style="left:787px;">
    <svg width="62" height="62" viewBox="0 0 62 62">
      <circle cx="31" cy="31" r="29" fill="#e0642a"/>
      <path d="M16 26c0-5 7-8 15-8s15 3 15 8l-6 2-2-4c-4-1-10-1-14 0l-2 4z" fill="#fff"/>
      <path d="M20 44l3-12h16l3 12z" fill="#fff"/>
      <circle cx="31" cy="37" r="3" fill="#e0642a"/>
    </svg>
    <p class="channel-text channel-phone">(11) 4020-7315</p>
  </div>

  <p class="form-lead">Preencha as informações abaixo que logo entraremos em contato...</p>

  <div class="field" style="top:975px;">Rafael Teixeira Moura Lima
    <svg width="16" height="16" viewBox="0 0 16 16"><circle cx="8" cy="8" r="7" fill="none" stroke="#5cb85c" stroke-width="1.6"/><path d="M4.5 8l2.3 2.3L11.5 5.6" fill="none" stroke="#5cb85c" stroke-width="1.8"/></svg>
  </div>
  <div class="field" style="top:1020px;">(11) 4471 20938
    <span class="field-error">Fill out a valid phone number</span>
    <svg width="16" height="16" viewBox="0 0 16 16"><circle cx="8" cy="8" r="7" fill="none" stroke="#d9372b" stroke-width="1.6"/><path d="M5.2 5.2l5.6 5.6M10.8 5.2l-5.6 5.6" stroke="#d9372b" stroke-width="1.8"/></svg>
  </div>
  <div class="field" style="top:1068px;">Rua das Acácias, 418
    <svg width="16" height="16" viewBox="0 0 16 16"><circle cx="8" cy="8" r="7" fill="none" stroke="#5cb85c" stroke-width="1.6"/><path d="M4.5 8l2.3 2.3L11.5 5.6" fill="none" stroke="#5cb85c" stroke-width="1.8"/></svg>
  </div>

  <div class="message-box">Escreva sua mensagem aqui !</div>
  <div class="submit-btn">SUBMIT</div>

  <footer class="footer-bar">
    <span class="footer-mark"></span>
    <span>Trilo Sistemas</span>
  </footer>

</body>
</html>
```